A simple and smart interface for busy teachers

We have an existing app (hybrid) on Apple Appstore and Google Playstore that we wish to refresh with some awesome designs and simplified screens.

We would like to stick to our existing colour scheme, see our website plovano.co.nz or screenshots on the appstore for more details and use of colours.

The uploaded files are current screens that we would like redesigned. Specifically, here are additional thoughts on what we wish to see:
1. With the Active Jobs screen, we would prefer to see a week-ly calendar style layout.
2. With Favourites, we would like to see each person's availability going across the page.

Target Market(s)

Middle aged women. (40+). New to tech users.

Industry/Entity Type

Education

Number of Pages Required

5+ page

Font styles to use
Sans Serif

Colors
ec1f27
474747
f78f20

Requirements
Must have
• Calendar view.
• Tidy and sharp info about the jobs.
Nice to have
• Simple and sharp.
Should not have
• Complicated graphics.
• Cluttered designs.
• Too much red. Screens should be mainly white(ish) with red and black.

```html
<!DOCTYPE html>
<html lang="en">
<head>
<meta charset="utf-8">
<title>Weekly Calendar</title>
<link href="https://fonts.googleapis.com/css2?family=Roboto:wght@300;400;500&display=swap" rel="stylesheet">
<style>
  :root {
    --brand-red: #d3362b;
    --ink: #1f1f1f;
    --ink-soft: #444444;
    --muted: #8a8a8a;
    --rule: #cfcfcf;
    --band: #f3f3f3;
    --paper: #ffffff;
    --toolbar: #454545;
  }
  * { margin: 0; padding: 0; box-sizing: border-box; }
  html, body { width: 675px; height: 1200px; overflow: hidden; background: var(--paper); }
  body { font-family: "Roboto", sans-serif; color: var(--ink); position: relative; }

  .app-bar { position: absolute; left: 0; top: 0; width: 675px; height: 95px; background: var(--brand-red); box-shadow: 0 2px 3px rgba(0,0,0,.18); z-index: 2; }
  .app-bar__back { position: absolute; left: 24px; top: 31px; }
  .app-bar__title { position: absolute; left: 0; right: 0; top: 26px; text-align: center; color: #fff; font-size: 31px; font-weight: 400; }

  .week-heading { position: absolute; left: 0; top: 95px; width: 675px; height: 156px; background: var(--band); border-bottom: 1px solid var(--rule); }
  .week-heading__month { position: absolute; left: 38px; top: 29px; font-size: 29px; font-weight: 300; color: var(--ink-soft); }
  .week-heading__range { position: absolute; left: 37px; top: 68px; font-size: 50px; font-weight: 300; color: #111; }

  .week-grid { position: absolute; left: 0; top: 251px; width: 675px; height: 841px; }
  .rule-v { position: absolute; left: 337px; top: 0; width: 1px; height: 841px; background: var(--rule); }
  .rule-h { position: absolute; left: 0; width: 675px; height: 1px; background: var(--rule); }

  .day { position: absolute; }
  .day__label { font-size: 27px; font-weight: 300; color: #111; white-space: nowrap; }
  .event { position: absolute; white-space: nowrap; font-size: 22px; }
  .event__title { color: var(--brand-red); }
  .event__time { color: var(--muted); font-size: 17px; }
  .event__tag { color: #111; font-size: 20px; }

  .mini-month { position: absolute; left: 337px; top: 857px; width: 338px; height: 235px; }
  .mini-month__name { position: absolute; left: 25px; top: 23px; font-size: 23px; font-weight: 300; }
  .mini-month__date { position: absolute; width: 26px; margin-left: -13px; text-align: center; font-size: 15px; color: #111; }
  .mini-month__date--other { color: var(--muted); }
  .mini-month__date--today { background: var(--brand-red); color: #fff; height: 22px; line-height: 22px; width: 23px; margin-left: -11px; }

  .toolbar { position: absolute; left: 0; top: 1092px; width: 675px; height: 108px; background: var(--toolbar); }
  .toolbar__icon { position: absolute; top: 28px; filter: drop-shadow(1px 2px 1px rgba(0,0,0,.5)); }
</style>
</head>
<body>
  <header class="app-bar">
    <svg class="app-bar__back" width="22" height="30" viewBox="0 0 22 30" aria-label="Back"><path d="M18 3 L6 15 L18 27" fill="none" stroke="#fff" stroke-width="4" stroke-linecap="round" stroke-linejoin="round"/></svg>
    <h1 class="app-bar__title">Weekly Calendar</h1>
  </header>

  <section class="week-heading">
    <p class="week-heading__month">November 2015</p>
    <p class="week-heading__range">this week next</p>
  </section>

  <main class="week-grid">
    <div class="rule-v"></div>
    <div class="rule-h" style="top:185px"></div>
    <div class="rule-h" style="top:401px"></div>
    <div class="rule-h" style="top:606px"></div>

    <div class="day" style="left:35px;top:28px"><p class="day__label">Mon 03</p></div>
    <div class="day" style="left:374px;top:28px"><p class="day__label">Tue 04</p></div>

    <div class="day" style="left:35px;top:205px;width:300px;height:190px">
      <p class="day__label">Wed 05</p>
      <p class="event event__time" style="left:1px;top:63px">02 : 30</p>
      <p class="event event__title" style="left:0;top:88px">Drawings Auditing</p>
    </div>
    <div class="day" style="left:374px;top:205px;width:300px;height:190px">
      <p class="day__label">Thu 06</p>
      <p class="event event__title" style="left:4px;top:74px">Pay Day</p>
    </div>

    <div class="day" style="left:35px;top:427px;width:300px;height:170px">
      <p class="day__label">Fri 07</p>
      <p class="event" style="left:1px;top:58px"><span class="event__tag">Pay Day</span> <span class="event__time">10:00</span></p>
      <p class="event event__title" style="left:0;top:94px">54463 - 24 - JH CA</p>
    </div>
    <div class="day" style="left:374px;top:427px;width:300px;height:170px">
      <p class="day__label">Sat 08</p>
      <p class="event" style="left:2px;top:58px"><span class="event__time">06:00</span>&nbsp; <span class="event__title">Maple Row Marke</span></p>
      <p class="event" style="left:2px;top:104px"><span class="event__time">05:00</span>&nbsp; <span class="event__title">Celebration of...</span></p>
    </div>

    <div class="day" style="left:35px;top:639px;width:300px;height:190px">
      <p class="day__label">Sun 09</p>
      <p class="event event__title" style="left:-2px;top:52px">Dana Whitcombe birthday</p>
    </div>

    <div class="mini-month">
      <p class="mini-month__name">June</p>
      <span class="mini-month__date mini-month__date--other" style="left:36px;top:62px">26</span>
      <span class="mini-month__date mini-month__date--other" style="left:80px;top:62px">27</span>
      <span class="mini-month__date mini-month__date--other" style="left:122px;top:62px">28</span>
      <span class="mini-month__date mini-month__date--other" style="left:165px;top:62px">29</span>
      <span class="mini-month__date mini-month__date--other" style="left:208px;top:62px">30</span>
      <span class="mini-month__date mini-month__date--other" style="left:252px;top:62px">31</span>
      <span class="mini-month__date" style="left:294px;top:62px">1</span>

      <span class="mini-month__date" style="left:36px;top:90px">2</span>
      <span class="mini-month__date" style="left:80px;top:90px">3</span>
      <span class="mini-month__date" style="left:122px;top:90px">4</span>
      <span class="mini-month__date" style="left:165px;top:90px">5</span>
      <span class="mini-month__date" style="left:208px;top:90px">6</span>
      <span class="mini-month__date" style="left:252px;top:90px">7</span>
      <span class="mini-month__date mini-month__date--today" style="left:294px;top:87px">8</span>

      <span class="mini-month__date" style="left:36px;top:118px">9</span>
      <span class="mini-month__date" style="left:80px;top:118px">10</span>
      <span class="mini-month__date" style="left:122px;top:118px">11</span>
      <span class="mini-month__date" style="left:165px;top:118px">12</span>
      <span class="mini-month__date" style="left:208px;top:118px">13</span>
      <span class="mini-month__date" style="left:252px;top:118px">14</span>
      <span class="mini-month__date" style="left:294px;top:118px">15</span>

      <span class="mini-month__date" style="left:36px;top:146px">16</span>
      <span class="mini-month__date" style="left:80px;top:146px">17</span>
      <span class="mini-month__date" style="left:122px;top:146px">18</span>
      <span class="mini-month__date" style="left:165px;top:146px">19</span>
      <span class="mini-month__date" style="left:208px;top:146px">20</span>
      <span class="mini-month__date" style="left:252px;top:146px">21</span>
      <span class="mini-month__date" style="left:294px;top:146px">22</span>

      <span class="mini-month__date" style="left:36px;top:174px">23</span>
      <span class="mini-month__date" style="left:80px;top:174px">24</span>
      <span class="mini-month__date" style="left:122px;top:174px">25</span>
      <span class="mini-month__date" style="left:165px;top:174px">26</span>
      <span class="mini-month__date" style="left:208px;top:174px">27</span>
      <span class="mini-month__date" style="left:252px;top:174px">28</span>
      <span class="mini-month__date" style="left:294px;top:174px">29</span>

      <span class="mini-month__date" style="left:36px;top:202px">30</span>
    </div>
  </main>

  <nav class="toolbar">
    <svg class="toolbar__icon" style="left:121px" width="46" height="46" viewBox="0 0 46 46" aria-label="Add event"><path d="M23 3 V43 M3 23 H43" stroke="#fff" stroke-width="4"/></svg>
    <svg class="toolbar__icon" style="left:238px" width="48" height="48" viewBox="0 0 48 48" aria-label="Day view"><rect x="3" y="7" width="42" height="37" fill="none" stroke="#fff" stroke-width="3.5"/><path d="M3 12 H45" stroke="#fff" stroke-width="3.5"/><path d="M13 2 V11 M35 2 V11" stroke="#fff" stroke-width="3.5"/></svg>
    <svg class="toolbar__icon" style="left:362px" width="48" height="48" viewBox="0 0 48 48" aria-label="Week view"><rect x="3" y="7" width="42" height="37" fill="none" stroke="#fff" stroke-width="3.5"/><path d="M3 12 H45 M17 7 V44 M31 7 V44" stroke="#fff" stroke-width="3.5"/><path d="M10 2 V11 M24 2 V11 M38 2 V11" stroke="#fff" stroke-width="3.5"/></svg>
    <svg class="toolbar__icon" style="left:482px" width="46" height="48" viewBox="0 0 46 48" aria-label="Month view"><rect x="3" y="7" width="40" height="37" rx="5" fill="none" stroke="#fff" stroke-width="3"/><path d="M3 14 H43" stroke="#fff" stroke-width="3"/><path d="M13 2 V10 M33 2 V10" stroke="#fff" stroke-width="3"/><g fill="#fff"><rect x="14" y="18" width="4" height="4"/><rect x="21" y="18" width="4" height="4"/><rect x="28" y="18" width="4" height="4"/><rect x="35" y="18" width="4" height="4"/><rect x="7" y="25" width="4" height="4"/><rect x="14" y="25" width="4" height="4"/><rect x="21" y="25" width="4" height="4"/><rect x="28" y="25" width="4" height="4"/><rect x="35" y="25" width="4" height="4"/><rect x="7" y="32" width="4" height="4"/><rect x="14" y="32" width="4" height="4"/><rect x="21" y="32" width="4" height="4"/><rect x="28" y="32" width="4" height="4"/></g></svg>
  </nav>
</body>
</html>
```